Q-Forma Stationary Package
Nimble Forma
Q-Forma Stationary Package - Internet Services
Creative Brief
Professional
Tom Gaskin
President and CEO
P.O. Box 4352 Burlington, NJ 08016
Tom.Gaskin@Q-FormaLLC.example
www.Q-FormaLLC.example
I am interested in seeing business card designs in both horizontal and vertical styles. My company provided technical consulting for the PGB Veterans, KRTU, KRTU Sergeants, KRTU Lieutenants and Halvern PD Senior Officers’ Association. I would like their logos on my card either on the front or the back listed under the words "Technical Consulting." You can find their logos located at https://www.filevault.example/s/83k2m1q7zpwe4tx/consulting.zip?dl=0. Unfortunately, some of these logos are only available from me in low-resolution.

```html
<!DOCTYPE html>
<html lang="en">
<head>
<meta charset="utf-8">
<title>Nimble Forma Business Card</title>
<link rel="stylesheet" href="https://fonts.googleapis.com/css2?family=Open+Sans:wght@400;600&display=swap">
<style>
  :root {
    --backdrop: #d9d9d9;
    --card-white: #ffffff;
    --card-black: #060606;
    --accent-blue: #2aa6d6;
    --text-grey: #6b6b6b;
  }
  html, body {
    margin: 0;
    padding: 0;
    width: 1200px;
    height: 902px;
    overflow: hidden;
    background: var(--backdrop);
    font-family: "Open Sans", Arial, sans-serif;
  }
  .canvas {
    position: relative;
    width: 1200px;
    height: 902px;
  }
  .card {
    position: absolute;
    left: 250px;
    width: 700px;
    height: 400px;
    box-shadow: 0 6px 18px rgba(0,0,0,0.18);
  }
  .card-back {
    top: 35px;
    background: var(--card-white);
  }
  .card-front {
    top: 467px;
    background: var(--card-black);
  }
  .contact-block {
    position: absolute;
    right: 48px;
    top: 70px;
    text-align: right;
    color: var(--text-grey);
    font-size: 15px;
    line-height: 27px;
  }
  .contact-email {
    display: inline-flex;
    align-items: center;
    gap: 8px;
  }
  .email-icon {
    width: 14px;
    height: 10px;
  }
  .website {
    position: absolute;
    left: 60px;
    top: 250px;
    color: var(--accent-blue);
    font-size: 22px;
    letter-spacing: 3px;
  }
  .holder {
    position: absolute;
    right: 48px;
    top: 175px;
    text-align: right;
    color: var(--accent-blue);
  }
  .holder-name {
    font-size: 24px;
    line-height: 34px;
  }
  .holder-role {
    font-size: 19px;
    line-height: 28px;
  }
  .brand {
    position: absolute;
    left: 40px;
    bottom: 42px;
    display: flex;
    align-items: center;
    gap: 12px;
  }
  .brand-dot {
    width: 30px;
    height: 30px;
    border-radius: 50%;
    background: var(--accent-blue);
  }
  .brand-name {
    color: var(--accent-blue);
    font-size: 30px;
    font-weight: 600;
    letter-spacing: 0.5px;
  }
</style>
</head>
<body>
<main class="canvas">
  <section class="card card-back">
    <div class="contact-block">
      <div class="contact-street">2207 Maple Hollow Rd</div>
      <div class="contact-city">Austin TX 78700</div>
      <div class="contact-phone">512.555.0147</div>
      <div class="contact-email">dana@sample.example
        <svg class="email-icon" viewBox="0 0 14 10" aria-hidden="true">
          <rect x="0" y="0" width="14" height="10" fill="#2aa6d6"/>
          <polyline points="0,0 7,6 14,0" fill="none" stroke="#ffffff" stroke-width="1.2"/>
        </svg>
      </div>
    </div>
    <div class="website">www.Sample.example</div>
  </section>

  <section class="card card-front">
    <div class="holder">
      <div class="holder-name">Dana Whitcombe</div>
      <div class="holder-role">Owner</div>
    </div>
    <div class="brand">
      <span class="brand-dot"></span>
      <span class="brand-name">Nimble Forma</span>
    </div>
  </section>
</main>
</body>
</html>
```